International printing supplier needs full stationery design

We would like a full stationery design to line up with our new logo and branding.
(In order to symbolise our responsiveness and fast service in the logo, we used an arrow as the accent on the “e“ in the company name.)

What designs we are looking for:
-font to be used in all documentation
-letterhead
-business card
-envelope TC4 (229x324 mm) and LC6 (114x162 mm)
-fax header
-email header
-smaller product labels (69x36mm and 104x73mm)
-bigger product label (A5)
-logo for email signature
-rubber stamp pattern
-flag pattern

Our company (Vóra) is B2B and is based in Central Europe. We operate in the printing press industry supplying press rooms with inks, additives and professional advice.

The design should thus communicate professionalism, responsiveness and swiftness.

Our current logo is attached and our main branding is based around the following colours:
Dark grey: RAL 7016
Orange: RAL 2004 (close to PMS 1655)
Light grey: RAL 9006 (or Pantone Cool Gray 10)

The Look and Feel Slider below should aid anyone in terms of what we imagined the stationery to look like.

Industry/Entity Type

Business

Requirements
Must have
• Logo should be clearly visible on all elements.

The designed or chosen font should match the logo's font and it should be easy to read.

The bigger product label must have an area coloured orange, which needs to contain (maximum 4) industry standard hazard symbols by law. Therefore, these legal constraints need to be included in the design of the product labels. It would be ideal if they could be integrated with the company's orange colour scheme and the rest of the stationery.
Nice to have
• The logo and slogan (Fényes lendülettel!®) should be presented together on all of the proposed designs.

The arrow in the logo would be an ideal symbol to use across the different elements.

The designs should be similar for all the different stationery elements, communicating a clear image and professionalism.
Should not have
• Expensive or impractical solutions in elements of the stationery (i.e. cut-outs, metallic font colours, special materials etc.) should be avoided.

Too many colours on each of the elements of the stationery are not needed, keep it simple.

```html
<!DOCTYPE html>
<html lang="en">
<head>
<meta charset="utf-8">
<title>Vóra – With Compliments Slip</title>
<link rel="stylesheet" href="https://fonts.googleapis.com/css2?family=Nunito:wght@600;700;800&display=swap">
<style>
  :root {
    --orange: #f5822f;
    --slate: #3f5568;
    --overlap: #4a2a12;
    --ink: #2f3a45;
    --paper: #ffffff;
  }
  html, body {
    margin: 0;
    padding: 0;
    overflow: hidden;
    background: var(--paper);
  }
  .slip {
    position: relative;
    width: 1200px;
    height: 567px;
    overflow: hidden;
    background: var(--paper);
    font-family: "Nunito", sans-serif;
    color: var(--ink);
  }
  .slip__artwork {
    position: absolute;
    left: 230px;
    top: 0;
    width: 475px;
    height: 567px;
    background: linear-gradient(160deg, var(--slate) 0%, var(--overlap) 45%, var(--orange) 80%);
  }
  .slip__greeting {
    position: absolute;
    left: 60px;
    top: 196px;
    margin: 0;
    font-size: 12px;
    font-weight: 800;
    color: var(--orange);
  }
  .contact {
    position: absolute;
    left: 940px;
    top: 56px;
    margin: 0;
    font-style: normal;
    font-size: 12px;
    font-weight: 700;
    line-height: 18.6px;
  }
  .contact__label,
  .contact__web {
    color: var(--orange);
  }
  .brand {
    position: absolute;
    left: 862px;
    top: 384px;
    width: 290px;
    text-align: center;
  }
  .brand__name {
    margin: 0;
    font-size: 96px;
    font-weight: 800;
    line-height: 1;
    letter-spacing: 0.02em;
    color: var(--orange);
  }
  .brand__slogan {
    margin: 14px 0 0;
    font-size: 12px;
    font-weight: 800;
    letter-spacing: 0.28em;
    text-transform: uppercase;
    color: var(--ink);
    white-space: nowrap;
  }
</style>
</head>
<body>
  <main class="slip">
    <div class="slip__artwork" role="img" aria-label="Artwork area: overlapping orange and slate upward arrow shapes with curved arrows"></div>

    <p class="slip__greeting">with compliments</p>

    <address class="contact">
      address line 01<br>
      address line 02<br>
      address line 03<br>
      postcode<br>
      <span class="contact__label">tel.</span> 01234 567 890<br>
      <span class="contact__label">fax.</span> 01234 567 890<br>
      <span class="contact__label">email.</span> info@vora.com<br>
      <span class="contact__web">www.vora.com</span>
    </address>

    <div class="brand">
      <p class="brand__name">Vóra</p>
      <p class="brand__slogan">Fényes lendülettel!®</p>
    </div>
  </main>
</body>
</html>
```